URGENT REQUEST Business Card for Executive Coach (already have logo)

Tavener Growth Advisory is a one person business doing high-end executive coaching, leadership training, and personal transformation work (psychotherapy). I urgently need new cards to fit my new logo.

I would like the card to be scannable by ScanTile and Quillbook Howdy.

A draft of the company website is at http://pruvex.net/demo/tavener

Target Market(s)

Senior corporate executives

Industry/Entity Type

Leadership

Requirements
Must have

• 1. Please use the company tag line: "The psychology of executive excellence"
2. My name is: Gregory Tavener, PhD (Kelbrook)
3. Behind my name, please make "(Kelbrook)" in smaller font.
4. My Title: Executive Coach & Leadership Trainer
4. No street address
5. If there is space, please put my current appointments:
Leadership Studies Faculty (CPA)
Supervisor & Coach (VORTEK)
6. Email: Gtavgreg@TavenerAdvisory.net
7. Web: www.TavenerAdvisory.net
8. Mobile: +65 8456-0000
Nice to have
• Company Tag Line:
• The psychology of executive excellence and personal transformation
• What I provide:
• Executive Coaching
• Leadership Training
• Personal Transformation

```html
<!DOCTYPE html>
<html lang="en">
<head>
<meta charset="utf-8">
<title>Tavener Growth Advisory – Business Card</title>
<link rel="stylesheet" href="https://fonts.googleapis.com/css2?family=Arimo:wght@400&display=swap">
<style>
  :root {
    --backdrop: #e6e4e1;
    --card: #f1f1f0;
    --ink-grey: #6e6e6e;
    --ink-soft: #858585;
    --accent-red: #8c1d1d;
    --shadow: rgba(0, 0, 0, 0.14);
  }
  * { margin: 0; padding: 0; box-sizing: border-box; }
  html, body {
    width: 1200px;
    height: 900px;
    overflow: hidden;
    background: var(--backdrop);
    font-family: "Arimo", Arial, sans-serif;
  }
  .stage {
    width: 1200px;
    height: 900px;
    display: flex;
    align-items: center;
    justify-content: center;
    gap: 40px;
  }
  .card {
    position: relative;
    width: 540px;
    height: 309px;
    background: var(--card);
    box-shadow: 0 6px 18px var(--shadow);
  }
  /* Front */
  .card--front {
    display: flex;
    align-items: center;
    justify-content: center;
  }
  .wordmark {
    color: var(--accent-red);
    font-weight: 400;
    letter-spacing: 0.06em;
    text-transform: uppercase;
    white-space: nowrap;
  }
  .card--front .wordmark { font-size: 26px; }
  /* Back */
  .identity {
    position: absolute;
    left: 40px;
    top: 48px;
  }
  .identity__name {
    font-size: 20px;
    font-weight: 400;
    color: var(--ink-grey);
    letter-spacing: 0.01em;
    white-space: nowrap;
  }
  .identity__school { font-size: 12px; }
  .identity__title {
    margin-top: 5px;
    font-size: 12px;
    color: var(--ink-soft);
  }
  .identity__rule {
    margin-top: 12px;
    width: 215px;
    height: 1px;
    background: var(--accent-red);
  }
  .contact {
    position: absolute;
    left: 40px;
    top: 134px;
    list-style: none;
    font-size: 12px;
    color: var(--ink-grey);
    line-height: 1.45;
  }
  .contact__label {
    display: inline-block;
    width: 16px;
    color: var(--accent-red);
  }
  .appointments {
    position: absolute;
    left: 40px;
    top: 206px;
    list-style: none;
    font-size: 12px;
    color: var(--ink-grey);
    line-height: 1.45;
  }
  .appointments__heading {
    font-size: 10.5px;
    color: var(--accent-red);
    letter-spacing: 0.05em;
    text-transform: uppercase;
    margin-bottom: 2px;
  }
  .brand {
    position: absolute;
    right: 30px;
    top: 118px;
    width: 230px;
  }
  .brand .wordmark { font-size: 14px; }
  .brand__tagline {
    margin-top: 6px;
    font-size: 10.5px;
    color: var(--ink-soft);
  }
  .brand__url {
    display: block;
    margin-top: 8px;
    font-size: 12px;
    color: var(--accent-red);
    text-decoration: none;
  }
</style>
</head>
<body>
  <main class="stage">
    <section class="card card--front" aria-label="Card front">
      <p class="wordmark">Tavener Growth Advisory</p>
    </section>

    <section class="card card--back" aria-label="Card back">
      <header class="identity">
        <h1 class="identity__name">Gregory Tavener, PhD <span class="identity__school">(Kelbrook)</span></h1>
        <p class="identity__title">Executive Coach &amp; Leadership Trainer</p>
        <div class="identity__rule"></div>
      </header>

      <ul class="contact">
        <li><span class="contact__label">m</span>+65 8456-0000</li>
        <li><span class="contact__label">e</span>Gtavgreg@TavenerAdvisory.net</li>
        <li><span class="contact__label">w</span>www.TavenerAdvisory.net</li>
      </ul>

      <ul class="appointments">
        <li class="appointments__heading">Current appointments</li>
        <li>Leadership Studies Faculty (CPA)</li>
        <li>Supervisor &amp; Coach (VORTEK)</li>
      </ul>

      <div class="brand">
        <p class="wordmark">Tavener Growth Advisory</p>
        <p class="brand__tagline">The psychology of executive excellence</p>
        <a class="brand__url" href="http://pruvex.net/demo/tavener">pruvex.net/demo/tavener</a>
      </div>
    </section>
  </main>
</body>
</html>
```